Dental Office needs Dynamic Wordpress Website Design

We need a a dynamic WordPress website design including SEO. We also need a mobile site. We would like the design to be easy to navigate, simple and modern. We would like to stick with a black, white and purple theme and existing logo and font. We have content and professional photos all ready to go as we would like to proceed asap.

Industry/Entity Type

Dental

```html
<!DOCTYPE html>
<html lang="en">
<head>
<meta charset="utf-8">
<title>Maple Creek Dental</title>
<link href="https://fonts.googleapis.com/css2?family=Roboto:wght@400;500;700&family=Varela+Round&display=swap" rel="stylesheet">
<style>
:root{
  --purple:#6b1a5e;
  --purple-dark:#5a1150;
  --nav-bg:#3a3a3a;
  --text:#555;
  --text-dark:#333;
  --orange:#e07a2e;
  --gray-bg:#e6e6e6;
  --light-bg:#f4f4f4;
  --footer:#0c0c0c;
  --white:#fff;
}
*{margin:0;padding:0;box-sizing:border-box}
html,body{width:900px;height:1200px;overflow:hidden}
body{font-family:'Roboto',Arial,sans-serif;color:var(--text);background:var(--white);position:relative}
.abs{position:absolute}
.top-strip{top:0;left:0;width:900px;height:5px;background:var(--purple)}
.header{top:5px;left:0;width:900px;height:92px;background:var(--white)}
.logo{left:149px;top:20px;display:flex;align-items:center;gap:10px}
.logo-mark{width:56px;height:56px;background:var(--purple)}
.logo-name{font-size:22px;font-weight:400;color:var(--purple);line-height:1.05;width:100px}
.contact-top{right:152px;top:31px;text-align:right;font-size:8px;color:var(--text-dark);line-height:19px}
.contact-top .accent{color:var(--purple)}
.contact-top svg{vertical-align:middle;margin-left:6px}
.nav{top:97px;left:0;width:900px;height:35px;background:var(--nav-bg)}
.nav ul{list-style:none;position:absolute;left:149px;top:0;display:flex;height:35px}
.nav li{font-size:7.5px;color:var(--white);line-height:35px;font-weight:500;padding:0 0 0 0}
.nav li.active{background:var(--purple)}
.hero{top:132px;left:0;width:900px;height:277px;background:linear-gradient(100deg,#d6c3b0 0%,#e8c9b8 35%,#9bc1c4 65%,#e8e4de 100%)}
.hero-arrow{top:100px}
.dots{left:427px;top:260px;display:flex;gap:5px}
.dots span{width:8px;height:8px;border-radius:50%;border:1px solid #fff}
.dots span.on{background:#fff}
.features{top:409px;left:0;width:900px;height:66px;background:var(--white)}
.feature{top:14px;display:flex;align-items:center;gap:30px}
.feature p{font-family:'Varela Round',sans-serif;font-size:13px;color:#555;line-height:16px}
.feature .ico{width:52px;height:52px;border-radius:50%;background:#f1f1f1;box-shadow:0 1px 3px rgba(0,0,0,.15);display:flex;align-items:center;justify-content:center}
.gray{top:475px;left:0;width:900px;height:311px;background:var(--gray-bg)}
h2{font-family:'Roboto',sans-serif;font-weight:700;font-size:12.5px;color:var(--purple)}
.photo{display:block}
.body-text{font-size:7.5px;line-height:13px;color:#666}
.more{font-size:7px;color:var(--orange)}
.welcome-more{color:var(--purple)}
.news-item{left:559px;display:flex;gap:10px}
.news-item .photo{width:57px;height:53px;border:1px solid #fff}
.news-item h3{font-size:7.5px;font-weight:700;color:#555;margin-top:3px;letter-spacing:.2px}
.news-item p{font-size:6.8px;line-height:8.5px;color:#777;margin:6px 0 3px}
.circle-btn{width:12px;height:12px;border-radius:50%}
.services{top:786px;left:0;width:900px;height:161px;background:var(--light-bg);border-top:1px solid #d8d8d8;border-bottom:1px solid #d8d8d8}
.svc{top:30px;width:127px}
.svc .photo{width:127px;height:68px}
.svc h4{font-size:8px;font-weight:700;color:#555;margin:13px 0 6px}
.svc p{font-size:7.5px;line-height:11px;color:#777}
.map{top:947px;left:0;width:900px;height:199px;background:linear-gradient(120deg,#ece9e3,#e3ded5 60%,#ebe5da)}
.contact-card{left:292px;top:40px;width:324px;height:119px;background:#fff;box-shadow:0 1px 3px rgba(0,0,0,.1)}
.contact-card .stripe{height:3px;background:repeating-linear-gradient(90deg,#c0392b 0 12px,#fff 12px 16px,#2c5f9e 16px 28px,#fff 28px 32px)}
.contact-card h2{font-weight:400;font-size:14px;text-align:center;margin-top:14px}
.contact-card dl{margin:16px 0 0 87px;font-size:7.6px;display:grid;grid-template-columns:47px auto;row-gap:6px;color:#222}
.contact-card dt{color:var(--purple)}
.footer{top:1146px;left:0;width:900px;height:54px;background:var(--footer)}
.footer .copy{left:150px;top:21px;font-size:8px;color:#fff}
.social{left:672px;top:17px;display:flex;gap:6px}
.social span{width:21px;height:21px;border-radius:50%;background:#e8e8e8}
</style>
</head>
<body>
<div class="abs top-strip"></div>

<header class="abs header">
  <div class="abs logo">
    <div class="logo-mark"></div>
    <div class="logo-name">Maple Creek Dental</div>
  </div>
  <div class="abs contact-top">
    <div><span class="accent">Call us directly:</span> 555-013-4720
      <svg width="7" height="10" viewBox="0 0 7 10"><rect x="0.5" y="0.5" width="6" height="9" rx="1" fill="none" stroke="#6a8fa8"/></svg></div>
    <div>118 Orchard Ave, Lindale, ON K0A 3R7 <span class="accent">View Location</span>
      <svg width="7" height="10" viewBox="0 0 7 10"><path d="M3.5 10C1 6 0 5 0 3.5a3.5 3.5 0 0 1 7 0C7 5 6 6 3.5 10z" fill="#6a8fa8"/><circle cx="3.5" cy="3.5" r="1.3" fill="#fff"/></svg></div>
  </div>
</header>

<nav class="abs nav">
  <ul>
    <li class="active" style="width:85px;text-align:center">Home</li>
    <li style="padding-left:11px;width:87px">About us</li>
    <li style="width:73px">Services</li>
    <li style="width:85px">Our Doctors</li>
    <li style="width:92px">Appointments</li>
    <li style="width:79px">Locations</li>
    <li>Contact Us</li>
  </ul>
</nav>

<section class="abs hero" role="img" aria-label="Photo of a dentist examining a smiling young girl in the dental chair">
  <svg class="abs hero-arrow" style="left:63px" width="14" height="24" viewBox="0 0 14 24"><path d="M12 2 3 12l9 10" fill="none" stroke="#fff" stroke-width="4"/></svg>
  <svg class="abs hero-arrow" style="left:834px" width="14" height="24" viewBox="0 0 14 24"><path d="m2 2 9 10-9 10" fill="none" stroke="#fff" stroke-width="4"/></svg>
  <div class="abs dots"><span class="on"></span><span></span><span></span></div>
</section>

<section class="abs features">
  <div class="abs feature" style="left:165px"><p>Make an<br>Appointment</p>
    <div class="ico"><svg width="26" height="24" viewBox="0 0 26 24"><rect x="1" y="3" width="24" height="20" rx="2" fill="#fff" stroke="#8ccbd6"/><rect x="1" y="3" width="24" height="5" fill="#6ec1d3"/></svg></div></div>
  <div class="abs feature" style="left:360px"><p>Check out our<br>Medical Services</p>
    <div class="ico"><svg width="28" height="28" viewBox="0 0 28 28"><path d="M11 2h6v8l7-4 3 5-7 3 7 3-3 5-7-4v8h-6v-8l-7 4-3-5 7-3-7-3 3-5 7 4z" fill="#3fb5cc"/></svg></div></div>
  <div class="abs feature" style="left:556px"><p>Meet the Staff:<br>Dr. Owen</p>
    <div class="ico"><svg width="26" height="24" viewBox="0 0 26 24"><rect x="3" y="2" width="20" height="20" rx="2" fill="#4fb9c9"/><circle cx="13" cy="10" r="3.5" fill="#fff"/><path d="M6 19c1-5 13-5 14 0z" fill="#fff"/></svg></div></div>
</section>

<section class="abs gray">
  <h2 class="abs" style="left:149px;top:17px">Welcome To Our Website</h2>
  <div class="abs photo" style="left:149px;top:48px;width:133px;height:76px;background:linear-gradient(90deg,#7a6a5c,#d8a898 60%,#e6a2ad)" role="img" aria-label="Portrait of the lead dentist"></div>
  <div class="abs" style="left:149px;top:131px;font-size:7.5px;color:#222">Dr. Daniel Whitford</div>
  <p class="abs body-text" style="left:286px;top:50px;width:245px">Mauris at justo eu lectus auctor porta vel ut libero. Suspe mattis tellus vel augue mollis ultrices. Suspendisse poten. Nunc erat enim, vestibulum vestibulum faucibus quis, rutrum. Nullam lacinia hend arcu, sed condimentum risus iaculis ut lorem ipsum solor clore lorem sipfum lorem sipusm dollor cifo.<br><span class="more welcome-more">Read More +</span></p>

  <h2 class="abs" style="left:149px;top:168px">Our Works</h2>
  <svg class="abs" style="left:504px;top:171px" width="30" height="12" viewBox="0 0 30 12"><circle cx="6" cy="6" r="6" fill="#777"/><path d="M7 3.5 4.5 6 7 8.5z" fill="#fff"/><circle cx="24" cy="6" r="6" fill="var(--purple)"/><path d="M23 3.5 25.5 6 23 8.5z" fill="#fff"/></svg>
  <div class="abs photo" style="left:149px;top:197px;width:149px;height:92px;background:linear-gradient(90deg,#e9d4c4,#c8dce6 55%,#e8eef2)" role="img" aria-label="Photo of dentists treating a patient"></div>
  <div class="abs" style="left:311px;top:201px;width:225px">
    <div style="font-size:8px;font-weight:700;color:#555;margin-bottom:7px">Mauris at justo eu lectus auctor</div>
    <p class="body-text">Mauris at justo eu lectus auctor porta vel ut libero. Suspe mattis tellus vel augue mollis ultrices. Suspendisse poten. Nunc erat enim, vestibulum vestibulum faucibus quis, rutrum. Nullam lacinia hend arcu,<br><span class="more">Read More +</span></p>
  </div>

  <h2 class="abs" style="left:560px;top:17px">NEWS &amp; BLOG</h2>
  <div class="abs news-item" style="top:46px"><div class="photo" style="background:linear-gradient(135deg,#f3d8c8,#c9795e)" role="img" aria-label="Close-up of a dental check"></div><div><h3>SUSPENDISSE MATTIS TELI</h3><p>Suspendisse mattis tellus vel augue<br>mollis ultrices suspends</p><span class="more">Read More +</span></div></div>
  <div class="abs news-item" style="top:109px"><div class="photo" style="background:linear-gradient(135deg,#2d6d8c,#c99d86)" role="img" aria-label="Patient receiving treatment"></div><div><h3>SUSPENDISSE MATTIS TELI</h3><p>Suspendisse mattis tellus vel augue<br>mollis ultrices suspends</p><span class="more">Read More +</span></div></div>
  <div class="abs news-item" style="top:173px"><div class="photo" style="background:linear-gradient(135deg,#f0e6e0,#c98a84)" role="img" aria-label="Close-up of a bright smile"></div><div><h3>SUSPENDISSE MATTIS TELI</h3><p>Suspendisse mattis tellus vel augue<br>mollis ultrices suspends</p><span class="more">Read More +</span></div></div>
  <div class="abs news-item" style="top:236px"><div class="photo" style="background:linear-gradient(135deg,#f6ece8,#d58f86)" role="img" aria-label="Person flossing teeth"></div><div><h3>SUSPENDISSE MATTIS TELI</h3><p>Suspendisse mattis tellus vel augue<br>mollis ultrices suspends</p><span class="more">Read More +</span></div></div>
</section>

<section class="abs services">
  <svg class="abs" style="left:150px;top:61px" width="24" height="24" viewBox="0 0 24 24"><circle cx="12" cy="12" r="11" fill="#fff" stroke="#ddd"/><circle cx="12" cy="12" r="7" fill="#bbb"/><path d="M13.5 9 10.5 12l3 3z" fill="#fff"/></svg>
  <h2 class="abs" style="left:184px;top:30px">Our Services</h2>
  <p class="abs body-text" style="left:185px;top:49px;width:108px;font-size:7.3px;line-height:12px">Mauris at justo eu lectus auctor porta vel ut libero. Suspendisse mattis tellus vel augue mollis ultrices. Suspendisse potenti. Nunc erat enim, vestibulum.</p>
  <div class="abs svc" style="left:317px"><div class="photo" style="background:linear-gradient(135deg,#cfe3ef,#5e92b5)" role="img" aria-label="Smiling dentist in the clinic"></div><h4>Lorem ipsum dolor ipsukm</h4><p>Porta vel ut libero. Suspendisse mattis tellus vel augue mollis</p></div>
  <div class="abs svc" style="left:455px"><div class="photo" style="background:linear-gradient(135deg,#2f85c0,#e2ccc0)" role="img" aria-label="Dentist treating a patient"></div><h4>Lorem ipsum dolor ipsukm</h4><p>Porta vel ut libero. Suspendisse mattis tellus vel augue mollis</p></div>
  <div class="abs svc" style="left:594px"><div class="photo" style="background:linear-gradient(135deg,#3c8ec7,#eef2f4)" role="img" aria-label="Dentist with a young child"></div><h4>Lorem ipsum dolor ipsukm</h4><p>Porta vel ut libero. Suspendisse mattis tellus vel augue mollis</p></div>
  <svg class="abs" style="left:727px;top:61px" width="24" height="24" viewBox="0 0 24 24"><circle cx="12" cy="12" r="11" fill="#fff" stroke="#ddd"/><circle cx="12" cy="12" r="9" fill="var(--purple)"/><path d="M10.5 9 13.5 12l-3 3z" fill="#fff"/></svg>
</section>

<section class="abs map" role="img" aria-label="Street map showing the office location">
  <div class="abs contact-card">
    <div class="stripe"></div>
    <h2>~ &nbsp;&nbsp;&nbsp;&nbsp;Contact Us&nbsp;&nbsp;&nbsp;&nbsp; ~</h2>
    <dl>
      <dt>Address :</dt><dd>118 Orchard Ave, Lindale, ON K0A 3R7</dd>
      <dt>Phone:</dt><dd>555-013-4720</dd>
      <dt>Email:</dt><dd>hello@maplecreekdental.example</dd>
    </dl>
  </div>
</section>

<footer class="abs footer">
  <div class="abs copy">© 2014 Lindale Studio All Rights Reserved</div>
  <div class="abs social"><span></span><span></span><span></span></div>
</footer>
</body>
</html>
```